Marcus Delvecchio Wellness podcast

I have overcome many health challenges. All of them have put me in position to help other people do the same. Eventually I became a certified health coach through the Academy of Integrative Nourishment. I have a strong desire to help because I know what it’s like to not feel well, and do what you want. The content on this sight will equip you with the tools to live a life full of health, freedom, and happiness. Complex health topics are broken down into simple ways to understand. No wellness topic is off limits, whether its heart disease, cancer, diabetes, sleep, hormones, or any other wellness topic.

Target Market(s)

People who are interested in growth and getting healthier

Industry/Entity Type

Health and Wellness

Colors
0054AA
0677BA
7BADD7
CADEEF
E8F1F8
0094D4
00A9DD
6FCCEA
C7EBF8
E9F6FB

Requirements

```html
<!DOCTYPE html>
<html lang="en">
<head>
<meta charset="UTF-8">
<title>Marcus Delvecchio Wellness Podcast</title>
<link href="https://fonts.googleapis.com/css2?family=Bebas+Neue&family=Poppins:wght@400&display=swap" rel="stylesheet">
<style>
  :root {
    --brand-blue: #0054AA;
    --ink: #1d1d1d;
    --sky-pale: #E9F6FB;
    --sky-soft: #C7EBF8;
    --sky-mid: #6FCCEA;
    --rule: #5a6670;
    --shirt-light: #e4e4e2;
    --shirt-shade: #c9c9c6;
  }
  html, body {
    margin: 0;
    padding: 0;
    width: 1200px;
    height: 1200px;
    overflow: hidden;
    background: #ffffff;
  }
  .cover {
    position: relative;
    width: 1200px;
    height: 1200px;
  }
  .cover svg {
    display: block;
  }
  .headline-name {
    font-family: "Bebas Neue", "Oswald", sans-serif;
  }
  .headline-first {
    fill: var(--brand-blue);
    stroke: #ffffff;
    stroke-width: 3;
    paint-order: stroke;
  }
  .headline-last,
  .headline-brand {
    fill: var(--ink);
  }
  .podcast-label {
    font-family: "Poppins", sans-serif;
    font-weight: 400;
    fill: var(--ink);
  }
  .mic-icon {
    stroke: #3b3b3b;
    fill: none;
    stroke-width: 6;
    stroke-linecap: round;
    stroke-linejoin: round;
  }
</style>
</head>
<body>
<div class="cover">
  <svg width="1200" height="1200" viewBox="0 0 1200 1200" xmlns="http://www.w3.org/2000/svg">
    <defs>
      <radialGradient id="sky-wash" cx="0.45" cy="0.35" r="0.85">
        <stop offset="0" stop-color="#ffffff"/>
        <stop offset="0.45" stop-color="var(--sky-pale)"/>
        <stop offset="0.8" stop-color="var(--sky-soft)"/>
        <stop offset="1" stop-color="var(--sky-mid)"/>
      </radialGradient>
      <linearGradient id="host-tone" x1="0" y1="0" x2="0" y2="1">
        <stop offset="0" stop-color="#8a6a4f"/>
        <stop offset="0.2" stop-color="#d9a88b"/>
        <stop offset="0.32" stop-color="var(--shirt-light)"/>
        <stop offset="1" stop-color="var(--shirt-shade)"/>
      </linearGradient>
    </defs>

    <!-- background -->
    <rect class="backdrop" width="1200" height="1200" fill="url(#sky-wash)"/>

    <!-- corner accents -->
    <polygon class="accent-top-left" points="0,0 258,0 0,360" fill="var(--brand-blue)"/>
    <polygon class="accent-right-band" points="1200,235 1200,1200 473,1200" fill="var(--brand-blue)"/>

    <!-- host portrait area -->
    <path class="host-portrait" role="img" aria-label="Portrait photo of the host, smiling, wearing a light grey t-shirt"
          d="M905,97 C1010,97 1035,160 1030,250 L1030,370 C1110,400 1200,420 1200,430 L1200,1200 L800,1200 L790,820 L792,470 C850,440 880,420 880,400 L865,300 C855,180 850,97 905,97 Z"
          fill="url(#host-tone)"/>

    <!-- headline -->
    <text class="headline-name headline-first" x="66" y="354" font-size="249">MARCUS</text>
    <text class="headline-name headline-last" x="66" y="521" font-size="210" textLength="693" lengthAdjust="spacingAndGlyphs">DELVECCHIO</text>
    <text class="headline-name headline-brand" x="66" y="699" font-size="224" textLength="684" lengthAdjust="spacingAndGlyphs">WELLNESS</text>

    <!-- divider -->
    <line class="divider" x1="66" y1="756" x2="749" y2="756" stroke="var(--rule)" stroke-width="1"/>

    <!-- microphone icon -->
    <g class="mic-icon">
      <line x1="70" y1="832" x2="70" y2="888"/>
      <line x1="85" y1="820" x2="85" y2="900"/>
      <line x1="100" y1="842" x2="100" y2="878"/>
      <line x1="178" y1="842" x2="178" y2="878"/>
      <line x1="193" y1="820" x2="193" y2="900"/>
      <line x1="208" y1="832" x2="208" y2="888"/>
      <rect x="120" y="822" width="38" height="78" rx="19"/>
      <line x1="140" y1="842" x2="150" y2="842"/>
      <line x1="140" y1="856" x2="150" y2="856"/>
      <line x1="140" y1="870" x2="150" y2="870"/>
      <path d="M108,872 C108,910 170,910 170,872"/>
      <line x1="139" y1="906" x2="139" y2="928"/>
      <path d="M118,940 L160,940 L156,928 L122,928 Z"/>
    </g>

    <!-- podcast label -->
    <text class="podcast-label" x="67" y="1013" font-size="64" textLength="350" lengthAdjust="spacing">PODCAST</text>
  </svg>
</div>
</body>
</html>
```